Al Qarmani our website www.klorvin.com

We need a Web Design for a new company called 'KLORVIN'. We develop innovative uPhone applications for consumers. Our initial product is PennyWise - an application that helps people manage their budgets and save money. We would like to see designs that use the color green. The final design should communicate financial safety and growth”.

Target Market(s)

technology and Electrics

Number of Pages Required

1 page

Requirements
Must have
• And work for pomelo and robotix
• To working min 2 languages Arabic and English
Nice to have
Should not have

```html
<!DOCTYPE html>
<html lang="en">
<head>
<meta charset="utf-8">
<title>KLORVIN — PennyWise</title>
<link href="https://fonts.googleapis.com/css2?family=Poppins:wght@300;400;500;600&display=swap" rel="stylesheet">
<style>
:root{
  --hero-start:#2a5ec9;
  --hero-end:#7d3b96;
  --blue:#1d6fd8;
  --green:#7cbf3e;
  --ink:#1f1f1f;
  --text:#5a5a5a;
  --light:#f2f2f2;
  --white:#ffffff;
  --footer:#050505;
  --card-line:#e6e6e6;
}
*{margin:0;padding:0;box-sizing:border-box}
html,body{width:1200px;height:3340px;overflow:hidden}
body{position:relative;font-family:'Poppins',sans-serif;color:var(--text);background:var(--white)}
.abs{position:absolute}

/* hero */
.hero{position:absolute;left:0;top:0;width:1200px;height:597px;background:linear-gradient(90deg,var(--hero-start) 0%,#4a4fb6 55%,var(--hero-end) 100%)}
.brand{position:absolute;display:flex;align-items:center;gap:12px;color:var(--white);font-family:'Poppins',sans-serif;font-weight:600;letter-spacing:4px}
.brand-dot{width:16px;height:16px;border-radius:50%;background:var(--green)}
.hero .brand{left:89px;top:36px;font-size:24px}
.nav{position:absolute;top:38px;left:0;width:1200px;height:24px;font-size:15px;color:var(--white);letter-spacing:0.5px}
.nav span{position:absolute;transform:translateX(-50%);white-space:nowrap}
.nav .active::after{content:"";position:absolute;left:0;right:0;bottom:-8px;height:2px;background:var(--green)}
.hero-title{left:176px;top:200px;font-size:64px;font-weight:600;color:var(--white)}
.hero-copy{left:176px;top:304px;width:420px;font-size:15px;line-height:24px;color:#e8ecff;font-weight:300}
.store{position:absolute;top:400px;height:54px;border:2px solid var(--white);border-radius:8px}
.store-a{left:176px;width:174px}
.store-b{left:370px;width:184px}
.hero-note{left:176px;top:476px;font-size:12px;color:#cfd7ff;font-weight:300}
.device{position:absolute;border-radius:40px;background:linear-gradient(180deg,#2a2a2a,#0f0f0f);box-shadow:0 10px 30px rgba(0,0,0,.3)}
.device-screen{position:absolute;left:16px;right:16px;top:62px;bottom:80px;background:linear-gradient(180deg,#1aa8ec,#0b86d8)}

/* intro features */
.intro-item{position:absolute;top:730px;width:340px;text-align:center}
.intro-item svg{display:block;margin:0 auto}
.intro-item h3{margin-top:18px;font-size:21px;font-weight:500;color:var(--ink)}
.intro-item p{margin:16px auto 0;width:290px;font-size:13px;line-height:21px}

/* about */
.about-photo{left:0;top:1002px;width:586px;height:534px;background:linear-gradient(135deg,#9aa0a6 0%,#c9c5c0 45%,#e6e3df 100%)}
.about{left:586px;top:1002px;width:614px;height:534px;background:var(--light)}
.about-title{left:699px;top:1080px;width:420px;font-size:42px;line-height:44px;font-weight:500;color:var(--ink)}
.about-copy{left:699px;top:1196px;width:380px;font-size:13px;line-height:21px}
.about-sub{left:699px;font-size:20px;color:var(--green);font-weight:400}

/* devices */
.devices{left:0;top:1536px;width:1200px;height:485px;background:var(--blue)}
.devices-title{left:176px;top:1636px;font-size:42px;line-height:46px;font-weight:600;color:var(--white)}
.devices-copy{left:176px;top:1752px;width:380px;font-size:13px;line-height:21px;color:#dbe8ff;font-weight:300}
.devices-note{left:263px;top:1872px;width:320px;font-size:13px;line-height:21px;color:#dbe8ff;font-weight:300}

/* features */
.features-title{left:0;top:2196px;width:1200px;text-align:center;font-size:42px;font-weight:500;color:var(--ink)}
.features-sub{left:0;top:2270px;width:1200px;text-align:center;font-size:16px}
.card{position:absolute;width:236px;height:248px;background:var(--white);box-shadow:0 2px 10px rgba(0,0,0,.08);text-align:center}
.card.is-active{border-top:3px solid var(--green)}
.card svg{display:block;margin:50px auto 0}
.card h4{margin-top:18px;font-size:20px;font-weight:500;color:var(--ink)}
.card p{margin:14px auto 0;width:190px;font-size:13px;line-height:21px}

/* footer */
.footer{left:0;top:2909px;width:1200px;height:431px;background:var(--footer)}
.footer .brand{left:0;width:1200px;justify-content:center;top:3006px;font-size:24px}
.social{left:0;top:3074px;width:1200px;display:flex;justify-content:center;gap:16px}
.social span{width:12px;height:12px;border-radius:50%;background:var(--white)}
.copyright{left:0;top:3104px;width:1200px;text-align:center;font-size:12px;color:#cccccc;letter-spacing:1px}
.footer-rule{left:87px;top:3180px;width:1024px;height:1px;background:#2a2a2a}
.footer-fine{left:87px;top:3218px;width:1024px;font-size:10px;line-height:16px;color:#bdbdbd;font-weight:300}
</style>
</head>
<body>

<header class="hero">
  <div class="brand"><span class="brand-dot"></span>KLORVIN</div>
  <nav class="nav">
    <span class="active" style="left:452px">HOME</span>
    <span style="left:572px">PRODUCTS</span>
    <span style="left:690px">SHOP</span>
    <span style="left:804px">ABOUT US</span>
    <span style="left:953px">CONTACT US</span>
    <span style="left:1086px">BRAND</span>
  </nav>
  <h1 class="abs hero-title">PennyWise</h1>
  <p class="abs hero-copy">It is a long established fact that a reader will be distracted by the readable content of a page when looking at its layout.</p>
  <div class="store store-a" role="img" aria-label="App store badge"></div>
  <div class="store store-b" role="img" aria-label="App store badge"></div>
  <p class="abs hero-note">* Requires uOS 7.0 or higher</p>
</header>
<div class="device" style="left:741px;top:122px;width:283px;height:523px" role="img" aria-label="Phone showing the PennyWise budget screen"><div class="device-screen"></div></div>

<section>
  <div class="intro-item" style="left:79px">
    <svg width="60" height="60" viewBox="0 0 60 60" fill="none" stroke="#7cbf3e" stroke-width="2"><rect x="14" y="8" width="30" height="40"/><rect x="20" y="14" width="30" height="40" fill="#fff"/><path d="M26 26h18M26 33h18M26 40h12"/></svg>
    <h3>Lorem Ipsum</h3>
    <p>There are many variations of passages of Lorem Ipsum available, but the majority have suffered for alternation.</p>
  </div>
  <div class="intro-item" style="left:431px">
    <svg width="60" height="60" viewBox="0 0 60 60" fill="none" stroke="#7cbf3e" stroke-width="2"><rect x="12" y="14" width="30" height="40"/><rect x="17" y="19" width="20" height="8"/><path d="M17 34h4M25 34h4M33 34h4M17 41h4M25 41h4M33 41h4M17 48h4M25 48h4M33 48h4"/><circle cx="44" cy="14" r="8" fill="#fff"/><path d="M44 10v8"/></svg>
    <h3>Standard Chunk</h3>
    <p>There are many variations of passages of Lorem Ipsum available, but the majority have suffered for alternation.</p>
  </div>
  <div class="intro-item" style="left:780px">
    <svg width="60" height="60" viewBox="0 0 60 60" fill="none" stroke="#7cbf3e" stroke-width="2"><rect x="14" y="10" width="32" height="44"/><rect x="23" y="6" width="14" height="8" fill="#fff"/><path d="M20 22l2 2 4-4M30 22h10M20 32l2 2 4-4M30 32h10M20 42l2 2 4-4M30 42h10"/></svg>
    <h3>Sed Perspiciatis</h3>
    <p>There are many variations of passages of Lorem Ipsum available, but the majority have suffered for alternation.</p>
  </div>
</section>

<section>
  <div class="abs about-photo" role="img" aria-label="Photo of hands holding a tablet showing the budget app"></div>
  <div class="abs about"></div>
  <h2 class="abs about-title">Lorem Ipsum is simply dummy</h2>
  <p class="abs about-copy">Contrary to popular belief, Lorem Ipsum is not simply random text. It has roots in a piece of classical Latin literature from 45 BC, making it over 2000 years old.</p>
  <h3 class="abs about-sub" style="top:1282px">Standard Chunk</h3>
  <p class="abs about-copy" style="top:1322px">Ut enim ad minima veniam, quis nostrum lorem text exercitationem ullam corporis.</p>
  <h3 class="abs about-sub" style="top:1377px">Contrary Popular</h3>
  <p class="abs about-copy" style="top:1416px">Quis autem vel eum iure reprehenderit qui in ea voluptate velit esse quam nihil molestiae.</p>
</section>

<section>
  <div class="abs devices"></div>
  <h2 class="abs devices-title">Available On All<br>Your Devices</h2>
  <p class="abs devices-copy">Contrary to popular belief, Lorem Ipsum is not simply random text. It has roots in a piece of classical Latin literature from 45 BC, making it over 2000 years old.</p>
  <svg class="abs" style="left:178px;top:1865px" width="64" height="54" viewBox="0 0 64 54" fill="none" stroke="#ffffff" stroke-width="2"><rect x="14" y="2" width="46" height="32"/><path d="M28 42h18M37 34v8"/><rect x="2" y="18" width="18" height="32" fill="#1d6fd8"/><circle cx="11" cy="45" r="1.5"/></svg>
  <p class="abs devices-note">Ut enim ad minima veniam, quis nost lorem text exercitationem ullam.</p>
</section>
<div class="device" style="left:741px;top:1598px;width:283px;height:521px" role="img" aria-label="Phone showing the PennyWise invoices screen"><div class="device-screen"></div></div>

<section>
  <h2 class="abs features-title">Features In This App</h2>
  <p class="abs features-sub">Contrary to popular belief, Lorem Ipsum is not simply random text.</p>

  <div class="card" style="left:87px;top:2335px">
    <svg width="60" height="60" viewBox="0 0 60 60" fill="none" stroke="#333" stroke-width="2"><rect x="10" y="8" width="30" height="42"/><rect x="15" y="13" width="20" height="8"/><path d="M15 28h4M24 28h4M15 35h4M24 35h4M15 42h4M24 42h4"/><circle cx="42" cy="42" r="10" fill="#fff"/><path d="M42 37v10"/></svg>
    <h4>Calculation</h4><p>There are many variations of passages of Lorem Ipsum</p>
  </div>
  <div class="card is-active" style="left:349px;top:2335px">
    <svg width="60" height="60" viewBox="0 0 60 60" fill="none" stroke="#7cbf3e" stroke-width="2"><rect x="6" y="22" width="40" height="24"/><path d="M14 34h14M14 40h8"/><path d="M34 36l20-22 4 4-20 22-6 2z"/></svg>
    <h4>Bank Cheque</h4><p>There are many variations of passages of Lorem Ipsum</p>
  </div>
  <div class="card" style="left:612px;top:2335px">
    <svg width="60" height="60" viewBox="0 0 60 60" fill="none" stroke="#333" stroke-width="2"><ellipse cx="30" cy="34" rx="20" ry="14"/><path d="M22 48v6M38 48v6M26 24h8"/><circle cx="30" cy="12" r="5"/></svg>
    <h4>Saving</h4><p>There are many variations of passages of Lorem Ipsum</p>
  </div>
  <div class="card" style="left:875px;top:2335px">
    <svg width="60" height="60" viewBox="0 0 60 60" fill="none" stroke="#333" stroke-width="2"><rect x="8" y="10" width="44" height="30"/><path d="M14 34l8-8 6 4 10-12M20 40l-6 14M40 40l6 14M30 4v6"/></svg>
    <h4>Growth Cycle</h4><p>There are many variations of passages of Lorem Ipsum</p>
  </div>

  <div class="card" style="left:87px;top:2611px">
    <svg width="60" height="60" viewBox="0 0 60 60" fill="none" stroke="#333" stroke-width="2"><rect x="8" y="12" width="44" height="40"/><path d="M8 22h44M18 6v10M42 6v10"/><path d="M14 30h6M27 30h6M40 30h6M14 38h6M27 38h6M40 38h6M14 46h6M27 46h6"/></svg>
    <h4>Schedule Planning</h4><p>There are many variations of passages of Lorem Ipsum</p>
  </div>
  <div class="card" style="left:349px;top:2611px">
    <svg width="60" height="60" viewBox="0 0 60 60" fill="none" stroke="#333" stroke-width="2"><path d="M14 6h32v48l-5-4-5 4-6-4-5 4-6-4-5 4z"/><path d="M22 18h16M22 28h16M22 38h10"/></svg>
    <h4>Invoice</h4><p>There are many variations of passages of Lorem Ipsum</p>
  </div>
  <div class="card" style="left:612px;top:2611px">
    <svg width="60" height="60" viewBox="0 0 60 60" fill="none" stroke="#333" stroke-width="2"><rect x="26" y="8" width="28" height="24"/><path d="M32 26v-6M39 26v-10M46 26v-14"/><circle cx="14" cy="16" r="5"/><path d="M6 54V30h16v24M14 38v16"/></svg>
    <h4>Financially Growth</h4><p>There are many variations of passages of Lorem Ipsum</p>
  </div>
  <div class="card" style="left:875px;top:2611px">
    <svg width="60" height="60" viewBox="0 0 60 60" fill="none" stroke="#333" stroke-width="2"><rect x="6" y="16" width="48" height="28"/><circle cx="30" cy="30" r="7"/><path d="M12 22h4M44 38h4M10 50h40M10 10h40"/></svg>
    <h4>Cash Flow</h4><p>There are many variations of passages of Lorem Ipsum</p>
  </div>
</section>

<footer>
  <div class="abs footer"></div>
  <div class="brand"><span class="brand-dot"></span>KLORVIN</div>
  <div class="abs social"><span></span><span></span><span></span><span></span></div>
  <p class="abs copyright">Copyright 2018 &nbsp;|&nbsp; All Rights Reserved.</p>
  <div class="abs footer-rule"></div>
  <p class="abs footer-fine">PennyWise helps you plan each month with calm and clarity. Track spending, set savings goals, schedule bills and watch your growth over time. Your data stays private on your device and syncs only when you choose. Built for uPhone, pomelo and robotix devices, with full support for English and Arabic. Simple charts show where money goes, gentle reminders keep payments on time, and clear reports help you make better choices. Start small, stay steady, and let each saved coin add up to real financial safety for you and your family every single day.</p>
</footer>

</body>
</html>
```